Business Card Design Lanford Motors

Used car dealership, We buy, sell, trade and finance a cars.

Industry/Entity Type

Finance

Contact Information for Business Card

Lanford Motors, Buy, Sell, Trade, Finance, 318 Willowbend St, Brookhollow, VT, 00417, 555-318-6092, www.Lanford-Motors.example

Requirements
Must have
• Crown
Nice to have
• purple and gold colors

```html
<!DOCTYPE html>
<html lang="en">
<head>
<meta charset="utf-8">
<title>Lanford Motors — Business Card</title>
<link rel="stylesheet" href="https://fonts.googleapis.com/css2?family=Open+Sans:wght@400;600;700;800&display=swap">
<style>
  :root {
    --purple: #6a1fa0;
    --purple-deep: #5a1890;
    --gold: #e2b70a;
    --paper: #f4f4f4;
    --ink: #2b2b2b;
    --bg: #e7e8ea;
  }
  * { box-sizing: border-box; margin: 0; padding: 0; }
  html, body { width: 1200px; height: 1024px; overflow: hidden; }
  body {
    background: var(--bg);
    font-family: "Open Sans", Arial, sans-serif;
    position: relative;
  }
  .card {
    position: absolute;
    left: 215px;
    width: 770px;
    height: 440px;
    border-radius: 4px;
    box-shadow: 0 6px 18px rgba(0,0,0,0.18);
    overflow: hidden;
  }
  /* Front */
  .card-front {
    top: 48px;
    background: radial-gradient(ellipse at 55% 40%, #6e22a6 0%, var(--purple-deep) 100%);
    color: #fff;
    text-align: center;
  }
  .brand {
    position: absolute;
    left: 0; right: 0; top: 150px;
    display: flex; align-items: center; justify-content: center; gap: 14px;
  }
  .brand-dot {
    width: 16px; height: 16px; border-radius: 50%;
    background: var(--gold);
  }
  .brand-name {
    font-weight: 800;
    font-size: 46px;
    letter-spacing: 1px;
    line-height: 1;
  }
  .card-front .brand-name { color: #fff; }
  .tagline {
    position: absolute;
    left: 0; right: 0; top: 218px;
    font-size: 22px;
    letter-spacing: 0.5px;
  }
  .tagline .sep { color: var(--gold); margin: 0 8px; }
  .front-url {
    position: absolute;
    left: 0; right: 0; bottom: 52px;
    color: var(--gold);
    font-size: 20px;
  }
  /* Back */
  .card-back {
    top: 536px;
    background: linear-gradient(135deg, #fafafa 0%, #ececec 100%);
    color: var(--ink);
  }
  .card-back .brand {
    top: 52px; left: 56px; right: auto;
    justify-content: flex-start;
  }
  .card-back .brand-name { color: var(--purple); font-size: 38px; }
  .card-back .brand-dot { width: 14px; height: 14px; }
  .person { position: absolute; left: 56px; top: 128px; right: 56px; }
  .person-name {
    color: var(--purple);
    font-weight: 700;
    font-size: 26px;
  }
  .person-role {
    display: flex; align-items: center; gap: 10px;
    font-size: 17px; margin-top: 2px;
  }
  .person-role .rule { flex: 1; height: 2px; background: var(--gold); }
  .contact {
    position: absolute; left: 56px; top: 222px;
    list-style: none;
    font-size: 18px; line-height: 30px;
  }
  .contact li { display: flex; align-items: center; gap: 10px; }
  .contact .icon { width: 16px; height: 16px; flex: none; }
  .contact .indent { padding-left: 26px; }
  .band {
    position: absolute; left: 0; right: 0; bottom: 0; height: 26px;
    display: flex;
  }
  .band-purple { width: 40%; background: var(--purple); }
  .band-gold { flex: 1; background: var(--gold); }
</style>
</head>
<body>
  <section class="card card-front">
    <div class="brand">
      <span class="brand-dot"></span>
      <span class="brand-name">LANFORD MOTORS INC.</span>
    </div>
    <p class="tagline">Buy<span class="sep">•</span>Sell<span class="sep">•</span>Trade<span class="sep">•</span>Finance</p>
    <p class="front-url">www.Lanford-Motors.example</p>
  </section>

  <section class="card card-back">
    <div class="brand">
      <span class="brand-name">LANFORD MOTORS INC.</span>
      <span class="brand-dot"></span>
    </div>
    <div class="person">
      <p class="person-name">Dana Whitfield</p>
      <p class="person-role">Owner <span class="rule"></span></p>
    </div>
    <ul class="contact">
      <li class="indent">318 Willowbend St</li>
      <li class="indent">Brookhollow, VT 00417</li>
      <li>
        <svg class="icon" viewBox="0 0 16 16" aria-hidden="true"><path fill="#e2b70a" d="M3.5 1.5l2.5 0.5 1 3-1.6 1.2a8 8 0 0 0 4.4 4.4L11 9l3 1 .5 2.5-2 2C6.5 14 2 9.5 1.5 3.5z"/></svg>
        555-318-6092
      </li>
      <li>
        <svg class="icon" viewBox="0 0 16 16" aria-hidden="true"><circle cx="8" cy="8" r="6.5" fill="none" stroke="#e2b70a" stroke-width="1.6"/><path d="M1.5 8h13M8 1.5c-3 3.5-3 9.5 0 13M8 1.5c3 3.5 3 9.5 0 13" fill="none" stroke="#e2b70a" stroke-width="1.2"/></svg>
        www.Lanford-Motors.example
      </li>
    </ul>
    <div class="band"><span class="band-purple"></span><span class="band-gold"></span></div>
  </section>
</body>
</html>
```